Web Design Project

The aim of this project to design a website for a service that would offer services for small business and non profit organizations using opensource software that is weaved to work together in harmony.

The website name is: velisto.net

Tavrel in Arabic means: cabbage. Cabbage is composed of leaves, actually there is nothing except leaves. Each leave by itself is not called cabbage, but a collection of leaves that are organized in a central way would give us cabbage.

Same idea for Tavrel where open source software very well organized and integrated would create a new thing with a new value.
Updates

Target Market(s)

Small business, Europe, Africa, Far east and Middle east

Industry/Entity Type

Small Business

Requirements
Must have
• The website would offer the following sections:
* Home page
* Benefits: value of tavrel
* Applications: applications offered by tavrel
* Pricing
* Purchase
* Customer log in
* Support
- FAQ
- Knowledge base
- Forums
- Open tickets

Please take the following consideration in design:
* White should predominate
* Only black and the colors of logo are permitted (attched)
Nice to have
• Design is better to express:
* Openness
* Dynamic
* Usable
* Cost effective

```html
<!DOCTYPE html>
<html lang="en">
<head>
<meta charset="utf-8">
<title>Tavrel — Creating a new thing with a new value</title>
<link rel="stylesheet" href="https://fonts.googleapis.com/css2?family=Questrial&family=Open+Sans:wght@400;600;700&family=Oswald:wght@500;600&display=swap">
<style>
  :root {
    --green: #8cc924;
    --green-dark: #6fa61a;
    --blue: #0093dd;
    --yellow: #f9c20d;
    --magenta: #b7508f;
    --ink: #3b3b3b;
    --grey: #757575;
    --grey-light: #d6d2cc;
    --field: #f4f4f4;
    --field-line: #cfcfcf;
    --footer: #5b5b5b;
    --white: #ffffff;
  }
  * { box-sizing: border-box; margin: 0; padding: 0; }
  html, body { width: 1040px; height: 1200px; overflow: hidden; background: var(--white); }
  body { position: relative; font-family: "Open Sans", Arial, sans-serif; color: var(--ink); }

  /* header */
  .brand { position: absolute; left: 20px; top: 46px; display: flex; align-items: center; gap: 12px; }
  .brand-dot { width: 30px; height: 30px; border-radius: 50%; background: var(--green); }
  .brand-name { font-family: "Questrial", sans-serif; font-size: 40px; color: var(--ink); line-height: 1; }
  .utility { position: absolute; right: 26px; top: 18px; display: flex; gap: 12px; }
  .utility a { display: flex; flex-direction: column; align-items: center; font-family: Arial, sans-serif; font-size: 12px; color: var(--ink); text-decoration: none; gap: 3px; }
  .utility svg { width: 18px; height: 16px; }
  .tagline { position: absolute; right: 28px; top: 67px; font-family: "Questrial", sans-serif; font-size: 27px; color: var(--ink); }

  /* hero */
  .hero { position: absolute; left: 0; top: 115px; width: 1040px; height: 430px; background: var(--green); }
  .main-nav { position: absolute; left: 17px; top: 9px; display: flex; font-family: "Questrial", sans-serif; font-weight: 700; font-size: 17px; }
  .main-nav a { position: absolute; top: 0; height: 25px; line-height: 25px; color: var(--ink); text-decoration: none; white-space: nowrap; -webkit-text-stroke: 0.5px var(--ink); }
  .main-nav a.is-current { background: var(--blue); color: var(--white); -webkit-text-stroke: 0.5px var(--white); width: 100px; text-align: center; }
  .hero-title { position: absolute; left: 42px; top: 105px; font-family: "Questrial", sans-serif; font-size: 32px; font-weight: 400; color: var(--ink); }
  .hero-text { position: absolute; left: 43px; top: 155px; width: 500px; font-size: 14.6px; line-height: 18px; color: var(--ink); }
  .hero-button { position: absolute; left: 43px; top: 243px; width: 155px; height: 34px; border-radius: 4px; background: var(--ink); color: #dcef9e; font-family: "Questrial", sans-serif; font-weight: 700; font-size: 14.5px; line-height: 34px; text-align: center; }
  .hero-art { position: absolute; left: 633px; top: 74px; width: 374px; height: 336px; border-radius: 6px; background: linear-gradient(180deg, #3b3b3b 0%, #3b3b3b 78%, #4a4a4a 100%); }

  /* feature cards */
  .card { position: absolute; top: 573px; width: 319px; height: 189px; color: var(--white); border-top: 3px solid rgba(255,255,255,0.25); }
  .card--support { left: 17px; background: var(--yellow); }
  .card--apps { left: 360px; background: var(--blue); }
  .card--kb { left: 699px; background: var(--magenta); }
  .card-mark { position: absolute; right: 16px; top: 10px; width: 80px; height: 80px; border-radius: 50%; background: rgba(255,255,255,0.18); }
  .card-title { position: absolute; left: 15px; top: 20px; font-family: "Oswald", sans-serif; font-weight: 600; font-size: 27px; letter-spacing: -0.3px; text-transform: uppercase; }
  .card-text { position: absolute; left: 14px; top: 63px; width: 298px; font-size: 12.4px; line-height: 15.5px; }
  .card-more { position: absolute; left: 13px; top: 136px; width: 100px; height: 25px; border-radius: 13px; background: linear-gradient(#ffffff, #e7e7e7); border: 2px solid #d8d8d8; color: #6a6a6a; font-size: 9.5px; font-weight: 700; line-height: 21px; text-align: center; }

  /* lower sections */
  .panel { position: absolute; top: 822px; width: 323px; }
  .panel--contact { left: 15px; }
  .panel--news { left: 358px; }
  .panel--quotes { left: 698px; }
  .panel-rule { height: 5px; background: repeating-linear-gradient(135deg, var(--grey-light) 0 2px, transparent 2px 5px); }
  .panel-head { display: flex; align-items: center; gap: 14px; height: 55px; border-bottom: 1px solid var(--grey-light); padding-top: 4px; }
  .panel-head svg { width: 28px; height: 30px; flex: none; }
  .panel-head h2 { font-family: "Questrial", sans-serif; font-weight: 400; font-size: 25px; color: var(--grey); letter-spacing: 0.5px; }

  .field { position: absolute; left: -3px; width: 296px; height: 29px; border: 1px solid var(--field-line); border-radius: 4px; background: var(--field); font-size: 12.5px; color: var(--ink); padding: 7px 11px; }
  .field--name { top: 92px; }
  .field--email { top: 128px; }
  .field--message { top: 164px; height: 71px; }
  .send { position: absolute; left: -2px; top: 247px; width: 76px; height: 26px; border-radius: 13px; background: linear-gradient(#a4d851, var(--green-dark)); border: 2px solid #cfe7a6; color: var(--white); font-size: 9.5px; font-weight: 700; text-align: center; line-height: 22px; }

  .news-item { position: absolute; left: 2px; width: 320px; }
  .news-item--1 { top: 93px; }
  .news-item--2 { top: 200px; }
  .news-thumb { position: absolute; left: 0; top: 0; width: 70px; height: 70px; border: 1px solid #ddd; padding: 4px; background: var(--white); }
  .news-thumb span { display: block; width: 100%; height: 100%; }
  .news-thumb--arrow span { background: linear-gradient(135deg, #e7eedb, #8ec24c); }
  .news-thumb--globe span { background: linear-gradient(135deg, #d5eef9, #2f9bd3); }
  .news-date { position: absolute; left: 85px; top: 2px; font-size: 14.5px; font-weight: 700; color: var(--blue); white-space: nowrap; }
  .news-text { position: absolute; left: 85px; top: 24px; width: 232px; font-size: 12.4px; line-height: 15.5px; color: var(--ink); }

  .quote-mark { position: absolute; left: 2px; top: 74px; font-family: Georgia, serif; font-size: 96px; line-height: 1; color: #e6eaf3; }
  .quote-text { position: absolute; left: 34px; top: 91px; width: 290px; font-size: 12.4px; line-height: 15.5px; color: var(--ink); }
  .quote-text p + p { margin-top: 15px; }
  .quote-author { position: absolute; left: 34px; top: 227px; font-size: 12.4px; font-weight: 700; color: var(--blue); }

  /* footer */
  .site-footer { position: absolute; left: 0; top: 1151px; width: 1040px; height: 27px; background: var(--footer); color: var(--white); font-size: 11.5px; line-height: 27px; }
  .site-footer .copy { position: absolute; left: 329px; }
  .site-footer .links { position: absolute; left: 549px; }
</style>
</head>
<body>

<header class="site-header">
  <div class="brand">
    <span class="brand-dot"></span>
    <span class="brand-name">tavrel</span>
  </div>
  <nav class="utility">
    <a href="#login">
      <svg viewBox="0 0 18 16"><rect x="3" y="2" width="12" height="9" fill="#3b3b3b"/><rect x="1" y="12" width="16" height="2" fill="#3b3b3b"/></svg>
      login
    </a>
    <a href="#support">
      <svg viewBox="0 0 18 16"><circle cx="9" cy="5" r="4" fill="#3b3b3b"/><path d="M2 16 Q9 7 16 16Z" fill="#3b3b3b"/></svg>
      support
    </a>
    <a href="#faq">
      <svg viewBox="0 0 18 16"><text x="9" y="13" text-anchor="middle" font-family="Arial" font-weight="700" font-size="13" fill="#3b3b3b">?</text></svg>
      FAQ
    </a>
  </nav>
  <p class="tagline">Creating a new thing with a new value</p>
</header>

<section class="hero">
  <nav class="main-nav">
    <a class="is-current" style="left:0">home</a>
    <a style="left:132px">benefits</a>
    <a style="left:253px">applications</a>
    <a style="left:412px">pricing</a>
    <a style="left:525px">purchase</a>
    <a style="left:660px">knowledge base</a>
    <a style="left:855px">open tickets</a>
  </nav>
  <h1 class="hero-title">why use tavrel product?</h1>
  <p class="hero-text">Typi non habent claritatem insitam; est usus legentis in iis qui facit eorum claritatem. Investigationes demonstraverunt lectores legere me lius quod ii legunt saepius. Claritas est etiam processus dynamicus, qui sequitur mutationem consuetudium lectorum.</p>
  <a class="hero-button">purchase product</a>
  <div class="hero-art" role="img" aria-label="Illustration of a laptop whose screen shows a software disc with a mouse pointer"></div>
</section>

<article class="card card--support">
  <span class="card-mark"></span>
  <h3 class="card-title">24/7 Client Support</h3>
  <p class="card-text">Lorem ipsum dolor sit amet, consectetuer adipiscing elit, sed diam nonummy nibh euismod tincidunt ut laoreet dolore magna.</p>
  <a class="card-more">READ MORE</a>
</article>
<article class="card card--apps">
  <span class="card-mark"></span>
  <h3 class="card-title">Applications</h3>
  <p class="card-text">Duis autem vel eum iriure dolor in hendrerit in vulputate velit esse molestie consequat, vel illum dolore eu feugiat nulla facilisis at vero eros.</p>
  <a class="card-more">READ MORE</a>
</article>
<article class="card card--kb">
  <span class="card-mark"></span>
  <h3 class="card-title">Knowledge Base</h3>
  <p class="card-text">Ut wisi enim ad minim veniam, quis nostrud exerci tation ullamcorper suscipit lobortis nisl ut aliquip ex ea commodo consequat.</p>
  <a class="card-more">READ MORE</a>
</article>

<section class="panel panel--contact">
  <div class="panel-rule"></div>
  <div class="panel-head">
    <svg viewBox="0 0 28 30"><circle cx="14" cy="10" r="7" fill="#757575"/><path d="M1 30 Q14 12 27 30Z" fill="#757575"/><rect x="5" y="7" width="3" height="6" rx="1" fill="#8cc924"/><rect x="20" y="7" width="3" height="6" rx="1" fill="#8cc924"/></svg>
    <h2>CONTACT US</h2>
  </div>
  <div class="field field--name">Full Name</div>
  <div class="field field--email">Email Address</div>
  <div class="field field--message">Message</div>
  <a class="send">SEND</a>
</section>

<section class="panel panel--news">
  <div class="panel-rule"></div>
  <div class="panel-head">
    <svg viewBox="0 0 28 30"><rect x="3" y="6" width="22" height="20" rx="2" fill="none" stroke="#757575" stroke-width="2.5"/><rect x="3" y="6" width="22" height="6" fill="#757575"/><rect x="8" y="2" width="2.5" height="6" fill="#757575"/><rect x="17.5" y="2" width="2.5" height="6" fill="#757575"/><text x="14" y="23" text-anchor="middle" font-family="Arial" font-weight="700" font-size="9" fill="#757575">15</text></svg>
    <h2>LATEST NEWS</h2>
  </div>
  <div class="news-item news-item--1">
    <div class="news-thumb news-thumb--arrow"><span role="img" aria-label="Green arrow graphic for a news item"></span></div>
    <p class="news-date">Fri, January. 03</p>
    <p class="news-text">Lorem ipsum dolor sit amet, consectet adipiscing elit, sed diam nonummy nibh euismod tincidunt ut .</p>
  </div>
  <div class="news-item news-item--2">
    <div class="news-thumb news-thumb--globe"><span role="img" aria-label="Blue globe graphic for a news item"></span></div>
    <p class="news-date">Mon, December. 28</p>
    <p class="news-text">Lorem ipsum dolor sit amet, consectet adipiscing elit, sed diam nonummy nibh euismod tincidunt ut .</p>
  </div>
</section>

<section class="panel panel--quotes">
  <div class="panel-rule"></div>
  <div class="panel-head">
    <svg viewBox="0 0 28 30"><ellipse cx="14" cy="14" rx="12" ry="9" fill="#757575"/><path d="M6 20 L4 27 L12 21Z" fill="#757575"/></svg>
    <h2>TESTIMONIALS</h2>
  </div>
  <span class="quote-mark">“</span>
  <div class="quote-text">
    <p>Duis autem vel eum iriure dolor in hendrerit in vulputate velit esse molestie consequat, vel illum dolore eu feugiat nulla facilisis at vero eros et accumsan et iusto odio.</p>
    <p>Nam liber tempor cum soluta nobis eleifend option congue nihil imperdiet doming id quod mazim placerat facer possim assum.</p>
  </div>
  <p class="quote-author">mr. Dario Fenn (manager)</p>
</section>

<footer class="site-footer">
  <span class="copy">Copyright 2014. All rights reserved.</span>
  <span class="links">Privacy Policy | Terms of Use</span>
</footer>

</body>
</html>
```